Design graphics and Print for a line of Herb Seeds- Envelope Design

We need a set of herb seed envelopes designed for a new seed line we are launching.
The design will be both front and back

Envelope will be a colored ( green) ) envelope with white text
or a white or cream envelope in all black /and images text. Or can add some colors to the white envelope.

I have attached the die-cut of the seed envelope.
I have attached some images of envelopes I like. Please do not copy, these are just to give you an idea of what I like.

Please feel free to reach out to me if you have any questions.

Thank you

Target Market(s)

The design needs to classic that can translate to 3 different audiences. 1. young parents 2. hip, young single millennial 3. kids

Industry/Entity Type

Ecommerce

Font styles to use
Serif

Requirements
Must have
• Please use the herb - Parsley for the design
Icon, Text or both.

Front side must have:
1.either herb Icon or work Parsley or both- this will be the main attraction
2. company name- Tall Meadow Pantry
3. can use design elements
4. can use my logo on from or back or not at all. I

Backside must have:
1. social media tags
FB, Instagram and Pinterest ( use icons) @tallmeadowpantry

my website: www.tallmeadowpantry.example
this can be on from or back of the envelope.
Should not have
• please stay away from "county" flowery, old fashioned style designs

```html
<!DOCTYPE html>
<html lang="en">
<head>
<meta charset="utf-8">
<title>Tall Meadow Pantry – Parsley Seed Envelope</title>
<link rel="stylesheet" href="https://fonts.googleapis.com/css2?family=Amatic+SC:wght@400;700&family=PT+Sans:wght@400;700&display=swap">
<style>
  :root {
    --page: #f1f0ec;
    --paper: #fbfbf8;
    --wash-green: #b9d39c;
    --wash-light: #e4efd2;
    --wash-cream: #f1f0cf;
    --leaf: #6f9a45;
    --leaf-dark: #3f7a2c;
    --ribbon: #8fa964;
    --ink: #3a3a3a;
    --ink-soft: #4a4a4a;
    --fold: #8c8c8c;
  }
  * { margin: 0; padding: 0; box-sizing: border-box; }
  html, body { width: 1200px; height: 864px; overflow: hidden; background: var(--page); }
  .canvas { position: relative; width: 1200px; height: 864px; }
  .dieline { position: absolute; left: 0; top: 0; }

  .brand-seal {
    position: absolute; left: 371px; top: 268px; width: 94px; height: 94px;
    border: 3px solid var(--leaf); border-radius: 50%;
    display: flex; align-items: center; justify-content: center; text-align: center;
    font-family: "Amatic SC", sans-serif; font-weight: 700; font-size: 19px;
    line-height: 1; color: var(--leaf); padding: 12px;
  }
  .brand-name {
    position: absolute; left: 280px; top: 376px; width: 276px; text-align: center;
    font-family: "Amatic SC", sans-serif; font-weight: 700; font-size: 17px;
    letter-spacing: 2px; color: var(--ink);
  }
  .herb-description {
    position: absolute; left: 292px; top: 404px; width: 252px; text-align: center;
    font-family: "PT Sans", sans-serif; font-size: 9.4px; line-height: 12px; color: var(--ink);
  }
  .herb-facts {
    position: absolute; left: 292px; top: 479px; width: 252px; text-align: center;
    font-family: "PT Sans", sans-serif; font-size: 9.4px; color: var(--ink);
  }
  .social-row {
    position: absolute; left: 370px; top: 519px; width: 96px;
    display: flex; justify-content: space-between;
  }
  .social-dot { width: 19px; height: 19px; border: 1.5px solid var(--leaf); border-radius: 50%; }
  .social-handle {
    position: absolute; left: 292px; top: 549px; width: 252px; text-align: center;
    font-family: "PT Sans", sans-serif; font-size: 13px; color: var(--ink-soft);
  }
  .ribbon {
    position: absolute; height: 25px; background: var(--ribbon); color: #fff;
    font-family: "PT Sans", sans-serif; font-size: 11.5px;
    display: flex; align-items: center; justify-content: center;
    clip-path: polygon(0 0, 100% 0, 97% 50%, 100% 100%, 0 100%, 3% 50%);
  }
  .ribbon-back { left: 320px; top: 576px; width: 186px; }
  .ribbon-front { left: 624px; top: 574px; width: 207px; height: 28px; font-size: 12px; }

  .herb-illustration {
    position: absolute; left: 665px; top: 235px; width: 165px; height: 250px;
    border-radius: 45% 45% 40% 40%;
    background: radial-gradient(ellipse at 50% 40%, var(--leaf) 0%, var(--leaf-dark) 55%, rgba(63,122,44,0) 72%);
    opacity: 0.85;
  }
  .herb-title {
    position: absolute; left: 600px; top: 494px; width: 254px; text-align: center;
    font-family: "Amatic SC", sans-serif; font-weight: 700; font-size: 44px;
    letter-spacing: 7px; color: var(--ink);
  }
</style>
</head>
<body>
<main class="canvas">
  <svg class="dieline" width="1200" height="864" viewBox="0 0 1200 864" aria-hidden="true">
    <defs>
      <clipPath id="envelope-shape">
        <path id="envelope-path" d="M285,192 H560 L578,152 Q582,133 600,133 H872 Q890,133 892,152 L893,192 L935,195 Q955,197 955,215 V615 Q955,635 935,638 L893,645 L890,672 Q888,690 870,690 H605 Q587,690 585,672 L560,630 H285 Q265,630 265,610 V212 Q265,192 285,192 Z"/>
      </clipPath>
      <radialGradient id="wash-top-left" cx="0.5" cy="0.5" r="0.5">
        <stop offset="0" stop-color="var(--wash-green)" stop-opacity="0.9"/>
        <stop offset="1" stop-color="var(--wash-green)" stop-opacity="0"/>
      </radialGradient>
      <radialGradient id="wash-cream" cx="0.5" cy="0.5" r="0.5">
        <stop offset="0" stop-color="var(--wash-cream)" stop-opacity="1"/>
        <stop offset="1" stop-color="var(--wash-cream)" stop-opacity="0"/>
      </radialGradient>
      <radialGradient id="wash-light" cx="0.5" cy="0.5" r="0.5">
        <stop offset="0" stop-color="var(--wash-light)" stop-opacity="1"/>
        <stop offset="1" stop-color="var(--wash-light)" stop-opacity="0"/>
      </radialGradient>
    </defs>
    <g clip-path="url(#envelope-shape)">
      <rect x="260" y="130" width="700" height="565" fill="var(--paper)"/>
      <ellipse cx="300" cy="240" rx="170" ry="130" fill="url(#wash-top-left)"/>
      <ellipse cx="500" cy="250" rx="130" ry="90" fill="url(#wash-light)"/>
      <ellipse cx="720" cy="170" rx="220" ry="110" fill="url(#wash-cream)"/>
      <ellipse cx="930" cy="520" rx="150" ry="220" fill="url(#wash-top-left)"/>
      <ellipse cx="720" cy="660" rx="260" ry="90" fill="url(#wash-light)"/>
      <ellipse cx="300" cy="600" rx="120" ry="60" fill="url(#wash-light)"/>
      <ellipse cx="540" cy="610" rx="90" ry="50" fill="url(#wash-light)"/>
    </g>
    <use href="#envelope-path" fill="none" stroke="#d8d8d2" stroke-width="1"/>
    <rect x="560" y="192" width="333" height="438" fill="none" stroke="var(--fold)" stroke-width="0.8"/>
  </svg>

  <!-- Back panel -->
  <div class="brand-seal">Tall Meadow Pantry</div>
  <h2 class="brand-name">TALL MEADOW PANTRY</h2>
  <p class="herb-description">Parsley is a flowering plant native to the Mediterranean. Provides great nutritional value and offers many potential health benefits. Those lovely herbs will grow to a mature height of roughly 15 - 18 inches tall and will spread a good 8 to 12 inches wide</p>
  <p class="herb-facts">Anual Herb - Harvest: 40 - 60 days</p>
  <div class="social-row" aria-label="Social media">
    <span class="social-dot"></span><span class="social-dot"></span><span class="social-dot"></span>
  </div>
  <p class="social-handle">@tallmeadowpantry</p>
  <div class="ribbon ribbon-back">www.tallmeadowpantry.example</div>

  <!-- Front panel -->
  <div class="herb-illustration" role="img" aria-label="Watercolour illustration of a parsley sprig"></div>
  <h1 class="herb-title">PARSLEY</h1>
  <div class="ribbon ribbon-front">www.tallmeadowpantry.example</div>
</main>
</body>
</html>
```